Pellrow Strategies business card

I need a business card for my new strategic consulting LLC, Pellrow Strategies. We specialize in helping people who care about broadband technology and telecommunications policy, and we're based in Washington DC. I'm looking for a card that says smart, credible, future-facing and signals a high level of expertise. It's DC, so there's clearly a limit to how crazy we can go with this card, but I am looking for a design that reflects a company that is comfortable with technology, policy, and having a little bit fun. I'm uploading my logo below, and I'd like to have it be part of the card design in some fashion.
Target Market(s)
Telecommunications and technology policy professionals
Industry/Entity Type
Technology policy
Contact Information for Business Card
Name of business, my name (Colin Mabberly), email (colin@pellrowstrategies.example) , phone number (202-555-0148)phone number
Look and feel

```html
<!DOCTYPE html>
<html lang="en">
<head>
<meta charset="utf-8">
<title>Pellrow Strategies – Business Card</title>
<link href="https://fonts.googleapis.com/css2?family=Montserrat:wght@400;700&display=swap" rel="stylesheet">
<style>
  :root {
    --brand-blue: #0055a0;
    --brand-sun: #f6ae3d;
    --card-white: #ffffff;
    --ink-dark: #222a33;
    --stage: #2b2c2f;
  }
  * { box-sizing: border-box; margin: 0; padding: 0; }
  html, body {
    width: 1200px; height: 875px; overflow: hidden;
    background: var(--stage);
    font-family: "Montserrat", Arial, sans-serif;
  }
  .sheet {
    width: 1200px; height: 875px;
    display: flex; align-items: center; justify-content: center; gap: 40px;
  }
  .card {
    width: 560px; height: 320px;
    border-radius: 22px;
    position: relative;
    overflow: hidden;
  }
  .card--front { background: var(--brand-blue); }
  .card--back { background: var(--card-white); }

  .wordmark {
    display: flex; align-items: center; gap: 12px;
    font-weight: 700; white-space: nowrap;
  }
  .wordmark__dot {
    border-radius: 50%; background: var(--brand-sun); flex: none;
  }
  .card--front .wordmark {
    position: absolute; left: 50%; top: 50%;
    transform: translate(-50%, -50%);
    color: var(--card-white); font-size: 40px;
  }
  .card--front .wordmark__dot { width: 30px; height: 30px; }

  .card--back .wordmark {
    position: absolute; right: 34px; top: 36px;
    color: var(--brand-blue); font-size: 26px;
  }
  .card--back .wordmark__dot { width: 20px; height: 20px; }

  .details {
    position: absolute; left: 40px; bottom: 34px;
    color: var(--brand-blue);
  }
  .details__company, .details__person {
    font-weight: 700; font-size: 25px; line-height: 1.2;
  }
  .details__rule {
    width: 250px; height: 2px; background: var(--brand-blue);
    margin: 14px 0 14px;
  }
  .details__line {
    display: flex; align-items: center; gap: 8px;
    color: var(--ink-dark); font-size: 14px; line-height: 1.7;
  }
  .details__line svg { width: 13px; height: 13px; fill: var(--brand-blue); flex: none; }
</style>
</head>
<body>
<main class="sheet">
  <section class="card card--front" aria-label="Card front">
    <div class="wordmark">
      <span class="wordmark__name">Pellrow Strategies</span>
      <span class="wordmark__dot"></span>
    </div>
  </section>

  <section class="card card--back" aria-label="Card back">
    <div class="wordmark">
      <span class="wordmark__name">Pellrow Strategies</span>
      <span class="wordmark__dot"></span>
    </div>
    <div class="details">
      <p class="details__company">Pellrow Strategies</p>
      <p class="details__person">Colin Mabberly</p>
      <div class="details__rule"></div>
      <p class="details__line">
        <svg viewBox="0 0 16 16" aria-hidden="true"><path d="M1 6c0-2 3-3 7-3s7 1 7 3v1h-4V5.5H5V7H1zM3 8h10l1 6H2z"/></svg>
        202-555-0148
      </p>
      <p class="details__line">
        <svg viewBox="0 0 16 16" aria-hidden="true"><path d="M1 3h14v10H1zM2.5 4.5 8 9l5.5-4.5v-.1h-11z"/></svg>
        pellrowstrategies.example
      </p>
    </div>
  </section>
</main>
</body>
</html>
```